Brisket Glazing

Modern glazing company specializing in commercial fit outs, pool fencing, frameless showers and glass splash backs, im after a very young/modern logo, it doesnt have to be revelent to glazing and a classy "boss like" design for the card. thank you in advanced
Updates

im thinking carbon fiber back ground or something along that line with bright orange wording or something maybe, open to suggestions 

Industry/Entity Type

Fencing

Contact Information for Business Card

company name, name, phone and products

```html
<!DOCTYPE html>
<html lang="en">
<head>
<meta charset="utf-8">
<title>Brisket Glazing – Business Card</title>
<link rel="stylesheet" href="https://fonts.googleapis.com/css2?family=Saira+Extra+Condensed:wght@300;400;500&display=swap">
<style>
  :root {
    --stage: #d9d6d2;
    --card: #141414;
    --card-edge: #0b0b0b;
    --glow: rgba(255, 255, 255, 0.16);
    --orange: #f2701d;
    --orange-soft: rgba(242, 112, 29, 0.55);
  }
  * { box-sizing: border-box; margin: 0; padding: 0; }
  html, body {
    width: 1200px;
    height: 873px;
    overflow: hidden;
    background: var(--stage);
  }
  .stage {
    width: 1200px;
    height: 873px;
    display: flex;
    align-items: center;
    justify-content: center;
    gap: 60px;
  }
  .card {
    position: relative;
    width: 520px;
    height: 316px;
    border-radius: 4px;
    background: var(--card);
    box-shadow: 0 18px 40px rgba(0, 0, 0, 0.35);
    font-family: "Saira Extra Condensed", sans-serif;
    color: var(--orange);
    overflow: hidden;
  }
  .card__texture {
    position: absolute;
    inset: 0;
    background: linear-gradient(160deg, #1c1c1c 0%, var(--card) 55%, var(--card-edge) 100%);
  }

  /* Front: company name */
  .card--front .card__texture {
    background:
      radial-gradient(ellipse 190px 95px at 50% 52%, var(--glow), transparent 70%),
      linear-gradient(160deg, #1c1c1c 0%, var(--card) 55%, var(--card-edge) 100%);
  }
  .brand {
    position: absolute;
    inset: 0;
    display: flex;
    align-items: center;
    justify-content: center;
    gap: 12px;
  }
  .brand__dot {
    width: 14px;
    height: 14px;
    border-radius: 50%;
    background: var(--orange);
  }
  .brand__name {
    font-size: 34px;
    font-weight: 400;
    letter-spacing: 1px;
  }

  /* Back: contact details */
  .contact {
    position: absolute;
    top: 40px;
    right: 48px;
    text-align: right;
  }
  .contact__name {
    font-size: 44px;
    font-weight: 400;
    line-height: 1;
    text-shadow: 0 0 6px var(--orange-soft);
  }
  .contact__role {
    font-size: 20px;
    font-weight: 300;
    margin-top: 2px;
    text-shadow: 0 0 4px var(--orange-soft);
  }
  .contact__phone {
    font-size: 36px;
    font-weight: 400;
    letter-spacing: 1px;
    margin-top: 6px;
    text-shadow: 0 0 6px var(--orange-soft);
  }
  .products {
    position: absolute;
    left: 150px;
    bottom: 30px;
    text-align: center;
    font-size: 17px;
    font-weight: 300;
    line-height: 1.25;
  }
  .products__title {
    font-weight: 500;
    letter-spacing: 1px;
  }
</style>
</head>
<body>
  <main class="stage">
    <section class="card card--back" aria-label="Business card, contact side">
      <div class="card__texture" role="img" aria-label="Dark carbon fibre texture"></div>
      <div class="contact">
        <p class="contact__name">Dale Morgan</p>
        <p class="contact__role">owner</p>
        <p class="contact__phone">0400 512 378</p>
      </div>
      <ul class="products" style="list-style:none">
        <li class="products__title">PRODUCTS</li>
        <li>- Commercial fit outs</li>
        <li>- pool fencing</li>
        <li>- frameless showers</li>
        <li>and glass splash backs</li>
      </ul>
    </section>

    <section class="card card--front" aria-label="Business card, brand side">
      <div class="card__texture" role="img" aria-label="Dark carbon fibre texture with soft light"></div>
      <div class="brand">
        <span class="brand__dot"></span>
        <span class="brand__name">Brisket Glazing</span>
      </div>
    </section>
  </main>
</body>
</html>
```